Redesign (8 documents) attached with brand guidelines - very quick/easy job!

We have 8 flyers/documents that we need put into the style of our new brand (see attached). So this is a simple rebrand exercise - complete with our brand guidelines (see attached)

I would need the designer to sign an NDA prior to taking this piece of work as I will be sharing newly branded documents with you prior to market release.

If these are done well we would as the same designer to work on a z-card designed brochure/POS

Brief:

- These are documents that customers would need to complete in order to book a particular service
- If you use images (ideally from Pixmora, so we don’t have to pay for them!)
- Icon ideas enclosed
-All the content on the brochures is required: but if you think it would 'flow better' in a different order that is fine.

Customers interested in receiving a particular service

Work

• Brandon (see brand guide)

• A4
• New logo ideas
• Anything out of brand guidleines

```html
<!DOCTYPE html>
<html lang="en">
<head>
<meta charset="utf-8">
<title>Vitalora – Health Objectives</title>
<link href="https://fonts.googleapis.com/css2?family=Titillium+Web:wght@400;600;700&display=swap" rel="stylesheet">
<style>
  :root {
    --brand-blue: #1a9bbf;
    --brand-blue-dark: #1288ad;
    --brand-yellow: #f2e600;
    --frame-grey: #c9cacc;
    --text-grey: #4b4b4d;
    --soft-grey: #eeeff0;
    --white: #ffffff;
    --watermark: #f4f0a8;
  }
  * { box-sizing: border-box; margin: 0; padding: 0; }
  html, body { width: 848px; height: 1200px; overflow: hidden; background: var(--white); }
  body { font-family: "Titillium Web", Arial, sans-serif; color: var(--text-grey); }

  .page { position: relative; width: 848px; height: 1200px; overflow: hidden; background: var(--white); }

  .page-decor { position: absolute; inset: 0; width: 848px; height: 1200px; }

  .brand {
    position: absolute; left: 56px; top: 42px;
    display: flex; align-items: center; gap: 10px;
    font-weight: 700; font-size: 38px; letter-spacing: 1px;
    color: var(--brand-yellow); line-height: 1;
  }
  .brand-dot { width: 18px; height: 18px; border-radius: 50%; background: var(--brand-yellow); }

  .doc-title {
    position: absolute; right: 69px; top: 140px;
    font-size: 29px; font-weight: 700; color: var(--brand-blue); line-height: 1;
  }

  .field {
    position: absolute; display: flex; align-items: baseline;
    font-size: 14.5px; font-weight: 600; color: var(--text-grey); white-space: nowrap;
  }
  .field-line {
    flex: 1; margin-left: 3px;
    border-bottom: 1.5px dotted #777; height: 1px; transform: translateY(-3px);
  }
  .field--nutritionist { left: 424px; top: 238px; width: 355px; }
  .field--store { left: 424px; top: 286px; width: 355px; }
  .field--client { left: 71px; top: 330px; width: 330px; }
  .field--date { left: 424px; top: 330px; width: 355px; }

  .objectives {
    position: absolute; left: 67px; top: 365px; width: 716px; height: 782px;
    background: var(--frame-grey); border-radius: 14px; padding: 5px;
    display: flex; flex-direction: column; gap: 8px;
  }
  .reason { position: relative; flex: 1; display: flex; flex-direction: column; }
  .reason-head {
    height: 38px; background: var(--brand-blue); border-radius: 12px 12px 0 0;
    display: grid; grid-template-columns: 250px 1fr; align-items: center;
    color: var(--white); font-weight: 700; font-size: 15px;
  }
  .reason-head span:first-child { padding-left: 18px; }
  .reason-head span:last-child { padding-left: 12px; }
  .reason-rows { flex: 1; display: grid; grid-template-rows: repeat(4, 1fr); gap: 2px; }
  .reason-row { display: grid; grid-template-columns: 250px 1fr; gap: 2px; }
  .question, .answer { background: var(--white); border-radius: 10px; }
  .question {
    display: flex; align-items: center; padding: 0 14px 0 19px;
    font-size: 11.5px; line-height: 1.35; color: var(--text-grey);
  }
  .reason-mark {
    position: absolute; left: 410px; top: 120px; width: 150px; height: 150px;
    border-radius: 50%; background: var(--watermark); opacity: 0.55; pointer-events: none;
  }
</style>
</head>
<body>
<div class="page">
  <svg class="page-decor" viewBox="0 0 848 1200" aria-hidden="true">
    <defs>
      <linearGradient id="sweep" x1="0" y1="0" x2="1" y2="1">
        <stop offset="0" stop-color="#f1f2f3"/>
        <stop offset="1" stop-color="#ffffff"/>
      </linearGradient>
    </defs>
    <path d="M0,300 C180,170 420,60 848,22 V230 C520,260 250,360 0,560 Z" fill="url(#sweep)" opacity="0.8"/>
    <path d="M0,0 H848 V12 C560,20 250,90 0,278 Z" fill="var(--brand-blue)"/>
    <path d="M0,278 C250,90 560,20 848,12 V22 C560,34 260,112 0,302 Z" fill="var(--brand-yellow)"/>
    <path d="M300,1200 C500,1160 700,1120 848,1060 V1200 Z" fill="#f3f4f5"/>
    <path d="M640,1200 C720,1180 790,1160 848,1136 V1150 C790,1176 730,1192 690,1200 Z" fill="var(--brand-yellow)"/>
    <path d="M690,1200 C730,1192 790,1176 848,1150 V1200 Z" fill="var(--brand-blue)"/>
  </svg>

  <div class="brand"><span class="brand-dot"></span>VITALORA</div>

  <h1 class="doc-title">Health Objectives</h1>

  <div class="field field--nutritionist">Nutritionist’s name:<span class="field-line"></span></div>
  <div class="field field--store">Store location:<span class="field-line"></span></div>
  <div class="field field--client">Client’s name:<span class="field-line"></span></div>
  <div class="field field--date">Date of consultation:<span class="field-line"></span></div>

  <div class="objectives">
    <section class="reason">
      <div class="reason-head"><span>Reason 1</span><span>Your comments</span></div>
      <div class="reason-rows">
        <div class="reason-row"><div class="question">Symptom, issue or condition you want to address.</div><div class="answer"></div></div>
        <div class="reason-row"><div class="question">Duration - how long have you felt like this or experienced this symptom(s)?</div><div class="answer"></div></div>
        <div class="reason-row"><div class="question">Have you seen a doctor about this for a diagnosis? Did you receive any medical treatment?</div><div class="answer"></div></div>
        <div class="reason-row"><div class="question">Is there any background or extra health or lifestyle information that relates to this situation that you want your practitioner to know about? Please give details.</div><div class="answer"></div></div>
      </div>
      <span class="reason-mark"></span>
    </section>
    <section class="reason">
      <div class="reason-head"><span>Reason 2</span><span>Your comments</span></div>
      <div class="reason-rows">
        <div class="reason-row"><div class="question">Symptom, issue or condition you want to address.</div><div class="answer"></div></div>
        <div class="reason-row"><div class="question">Duration - how long have you felt like this or experienced this symptom(s)?</div><div class="answer"></div></div>
        <div class="reason-row"><div class="question">Have you seen a doctor about this for a diagnosis? Did you receive any medical treatment?</div><div class="answer"></div></div>
        <div class="reason-row"><div class="question">Is there any background or extra health or lifestyle information that relates to this situation that you want your practitioner to know about? Please give details.</div><div class="answer"></div></div>
      </div>
      <span class="reason-mark"></span>
    </section>
  </div>
</div>
</body>
</html>
```